Freelance business trainer needs a new business card

My business is called Tbrite. I provide training in the workplace on management, coaching and mentoring, and customer service topics for a variety of businesses, colleges and private training providers, and teach on management programs. I need a professional but eye catching business card. Business colours grey and orange. My name Linda Marchbank; Tel 07853 416207; email lmarchbank@tbrite.co.uk; website www.tbrite.co.uk.
Happy to have some sort of logo on front and details on back or all on one side
Target Market(s)
SME businesses and colleges - workshops i run are for adults in the workplace
Industry/Entity Type
Training
Look and feel

```html
<!DOCTYPE html>
<html lang="en">
<head>
<meta charset="utf-8">
<title>Tbrite business card</title>
<link href="https://fonts.googleapis.com/css2?family=Montserrat:wght@300;400;700;800&display=swap" rel="stylesheet">
<style>
  :root {
    --bg: #eeeeef;
    --card-white: #ffffff;
    --card-grey: #8c8d90;
    --orange: #f7941d;
    --text-light: #f4f4f4;
    --text-grey: #8a8b8e;
  }
  * { margin: 0; padding: 0; box-sizing: border-box; }
  html, body { width: 1200px; height: 1000px; overflow: hidden; }
  body {
    background: var(--bg);
    font-family: "Montserrat", sans-serif;
    position: relative;
  }
  .card {
    position: absolute;
    width: 540px;
    height: 309px;
    top: 345px;
    box-shadow: 0 6px 18px rgba(0,0,0,0.12);
    overflow: hidden;
  }
  .card-front { left: 40px; background: var(--card-white); }
  .card-back { left: 620px; background: var(--card-grey); }

  /* front */
  .front-brand {
    position: absolute;
    left: 0; right: 0; top: 105px;
    display: flex; align-items: center; justify-content: center; gap: 12px;
  }
  .brand-dot {
    width: 34px; height: 34px; border-radius: 50%;
    background: var(--orange);
  }
  .front-brand .brand-name {
    font-weight: 800; font-size: 40px; color: var(--text-grey); letter-spacing: 0.5px;
  }
  .front-band {
    position: absolute; left: 0; right: 0; bottom: 0; height: 34px;
    background: var(--card-grey);
    display: flex; align-items: center; justify-content: center;
  }
  .website { color: var(--text-light); font-size: 13px; font-weight: 400; letter-spacing: 0.5px; }

  /* back */
  .back-brand {
    position: absolute; left: 30px; top: 28px;
    display: flex; align-items: center; gap: 8px;
  }
  .back-brand .brand-dot { width: 26px; height: 26px; }
  .back-brand .brand-name { font-weight: 700; font-size: 18px; color: var(--text-light); }
  .wordmark {
    position: absolute; right: 40px; top: 118px;
    font-weight: 800; font-size: 44px; color: var(--text-light);
  }
  .person {
    position: absolute; left: 30px; top: 200px;
    padding-right: 16px; border-right: 1px solid var(--text-light);
  }
  .person-name { color: var(--orange); font-size: 15px; font-weight: 400; }
  .person-role { color: var(--text-light); font-size: 15px; font-weight: 300; margin-top: 2px; }
  .contacts {
    position: absolute; left: 225px; top: 202px;
    list-style: none;
  }
  .contacts li {
    display: flex; align-items: center; gap: 8px;
    color: var(--text-light); font-size: 13px; font-weight: 300;
    margin-bottom: 6px;
  }
  .contacts svg { width: 16px; height: 16px; flex: none; }
</style>
</head>
<body>

<section class="card card-front" aria-label="Card front">
  <div class="front-brand">
    <span class="brand-dot"></span>
    <span class="brand-name">Tbrite</span>
  </div>
  <div class="front-band"><span class="website">www.tbrite.co.uk</span></div>
</section>

<section class="card card-back" aria-label="Card back">
  <div class="back-brand">
    <span class="brand-dot"></span>
    <span class="brand-name">Tbrite</span>
  </div>
  <div class="wordmark">Tbrite</div>
  <div class="person">
    <p class="person-name">Linda Marchbank</p>
    <p class="person-role">Business trainer</p>
  </div>
  <ul class="contacts">
    <li>
      <svg viewBox="0 0 16 16" aria-hidden="true">
        <circle cx="8" cy="8" r="8" fill="#f7941d"/>
        <path d="M5.5 4.2h1.4l.7 2-.9.7a5 5 0 0 0 2.4 2.4l.7-.9 2 .7v1.4c0 .5-.4.8-.9.8A6.2 6.2 0 0 1 4.7 5.1c0-.5.3-.9.8-.9z" fill="#8c8d90"/>
      </svg>
      07853 416207
    </li>
    <li>
      <svg viewBox="0 0 16 16" aria-hidden="true">
        <circle cx="8" cy="8" r="8" fill="#f7941d"/>
        <rect x="4" y="5" width="8" height="6" rx="0.8" fill="#8c8d90"/>
        <path d="M4.3 5.4 8 8.3l3.7-2.9" stroke="#f7941d" stroke-width="0.9" fill="none"/>
      </svg>
      lmarchbank@tbrite.co.uk
    </li>
  </ul>
</section>

</body>
</html>
```